Security Warning Sign

We have an existing sign that needs an update. I have attached a picture of the current square sign. We need to maintain the same wording. It needs to be professional and appropriate to attach to our customers fence. Also attached is a copy of our building sign which may lend some inspiration and hopefully the ai format will assist. The final sign will be 600mm x 600mmOur website is www.halvorngate.com.au

```html
<!DOCTYPE html>
<html lang="en">
<head>
<meta charset="utf-8">
<title>Halvorngate Security Services – Surveillance Warning Sign</title>
<link rel="stylesheet" href="https://fonts.googleapis.com/css2?family=Alegreya+Sans:wght@800&family=Arimo:wght@700&family=Fira+Sans+Condensed:wght@700&display=swap">
<style>
  :root {
    --sign-red: #d42027;
    --sign-black: #000000;
    --sign-white: #ffffff;
    --page-bg: #ffffff;
  }
  html, body {
    margin: 0;
    padding: 0;
    width: 1200px;
    height: 1199px;
    overflow: hidden;
    background: var(--page-bg);
  }
  .sign {
    display: block;
    width: 1200px;
    height: 1199px;
  }
  .sign__rim { fill: var(--sign-black); }
  .sign__gap { fill: var(--sign-white); }
  .sign__face { fill: var(--sign-red); }
  .sign__headline {
    font-family: "Fira Sans Condensed", "Arial Narrow", sans-serif;
    font-weight: 700;
    font-size: 108px;
    fill: var(--sign-white);
    letter-spacing: 1px;
  }
  .sign__message {
    font-family: "Arimo", Arial, sans-serif;
    font-weight: 700;
    font-size: 55px;
    fill: var(--sign-white);
  }
  .sign__rule {
    stroke: var(--sign-white);
    stroke-width: 1.6;
  }
  .sign__phone {
    font-family: "Alegreya Sans", sans-serif;
    font-weight: 800;
    font-size: 58px;
    font-variant-numeric: oldstyle-nums;
    fill: var(--sign-white);
    letter-spacing: 1px;
  }
  .brand__mark { fill: var(--sign-white); }
  .brand__name {
    font-family: "Fira Sans Condensed", "Arial Narrow", sans-serif;
    font-weight: 700;
    font-size: 30px;
    fill: var(--sign-white);
  }
  .camera-icon { fill: var(--sign-white); opacity: 0.92; }
</style>
</head>
<body>
<svg class="sign" viewBox="0 0 855 854" preserveAspectRatio="none" xmlns="http://www.w3.org/2000/svg">
  <polygon class="sign__rim" points="258,15 598,15 840,258 840,598 598,840 258,840 15,598 15,258"/>
  <polygon class="sign__gap" points="263,27 593,27 828,263 828,593 593,828 263,828 27,593 27,263"/>
  <polygon class="sign__face" points="266,35 590,35 820,266 820,590 590,820 266,820 35,590 35,266"/>

  <text class="sign__headline" x="428" y="196" text-anchor="middle">WARNING</text>

  <g role="img" aria-label="Surveillance camera icon">
    <polygon class="camera-icon" points="60,262 78,236 186,296 168,322"/>
    <rect class="camera-icon" x="40" y="298" width="14" height="32"/>
    <polygon class="camera-icon" points="50,310 95,290 104,302 58,322"/>
  </g>

  <g class="sign__message" text-anchor="middle">
    <text x="428" y="279">ELECTRONIC</text>
    <text x="428" y="354">SURVEILLANCE</text>
    <text x="428" y="425">AND RECORDING</text>
    <text x="428" y="497">DEVICES INSTALLED</text>
    <text x="428" y="568">IN THIS AREA</text>
  </g>

  <line class="sign__rule" x1="200" y1="604" x2="655" y2="604"/>

  <text class="sign__phone" x="428" y="665" text-anchor="middle">1300 418 275</text>

  <g class="brand">
    <circle class="brand__mark" cx="330" cy="748" r="42"/>
    <text class="brand__name" x="396" y="731">HALVORNGATE</text>
    <text class="brand__name" x="396" y="762">SECURITY</text>
    <text class="brand__name" x="396" y="793">SERVICES</text>
  </g>
</svg>
</body>
</html>
```